Business Card for Holistic Health Business
Bright Ferns Natural Wellness & Live Cell Review
Use same font as used in my logo
Not sure, I am open to different fonts.
Simple
Marla Dunwoody
DynBC, CH, BA
Larkvale Acupuncture Clinic
2736-18 Avenue, Suite 200
Larkvale, AB T8K 2P6
brightferns@mailnest.ca
www.brightfernsnaturalwellness.com
Logo for Bright Ferns business card.

```html
<!DOCTYPE html>
<html lang="en">
<head>
<meta charset="utf-8">
<title>Bright Ferns Stationery</title>
<link href="https://fonts.googleapis.com/css2?family=Didact+Gothic&display=swap" rel="stylesheet">
<style>
:root{
  --bg:#eeeff1;
  --paper:#ffffff;
  --ink:#2b2b2b;
  --muted:#6b6b6b;
  --blue:#3f8fd6;
  --black:#0d0d0d;
  --shadow:rgba(0,0,0,.12);
}
*{margin:0;padding:0;box-sizing:border-box}
html,body{width:1200px;height:936px;overflow:hidden}
body{background:var(--bg);position:relative;font-family:"Didact Gothic",Arial,sans-serif;color:var(--ink)}
.sheet{position:absolute;background:var(--paper);box-shadow:0 2px 6px var(--shadow);overflow:hidden}
.swoosh{position:absolute;left:0;bottom:0;width:100%}
.brand{position:absolute;display:flex;align-items:center;gap:6px;white-space:nowrap}
.brand .dot{border-radius:50%;background:var(--blue);flex:none}
.brand .name{color:var(--ink);line-height:1}
.tagline{position:absolute;color:var(--muted);white-space:nowrap}
.web{position:absolute;left:0;width:100%;text-align:center;color:#fff;letter-spacing:.5px}
.contact{position:absolute;color:var(--muted);line-height:1.45;white-space:nowrap}

.letterhead{left:177px;top:71px;width:393px;height:617px}
.letterhead .brand{left:22px;top:26px}
.letterhead .dot{width:7px;height:7px}
.letterhead .name{font-size:16px}
.letterhead .tagline{left:22px;top:46px;font-size:6px}
.letterhead .contact{right:22px;top:26px;font-size:5px}
.letterhead .faint-mark{position:absolute;left:150px;top:170px;width:86px;height:86px;border-radius:50%;border:3px solid #e6e6e6}
.letterhead .swoosh{height:240px}
.letterhead .web{bottom:22px;font-size:7px}

.folder{left:633px;top:56px;width:506px;height:670px}
.folder .brand{left:180px;top:222px}
.folder .dot{width:12px;height:12px}
.folder .name{font-size:40px}
.folder .tagline{left:180px;top:268px;font-size:11px;border-top:1px solid #999;padding-top:3px}
.folder .swoosh{height:300px}
.folder .web{bottom:26px;font-size:9px}

.card-front{left:172px;top:724px;width:246px;height:81px}
.card-front .brand{left:12px;top:10px}
.card-front .dot{width:5px;height:5px}
.card-front .name{font-size:13px}
.card-front .tagline{left:12px;top:26px;font-size:4px}
.card-front .contact{left:12px;top:38px;font-size:4px}
.card-front .swoosh{height:34px}

.card-back{left:172px;top:820px;width:246px;height:78px;background:var(--blue)}
.card-back .brand{left:14px;top:16px}
.card-back .dot{width:6px;height:6px;background:#fff}
.card-back .name{font-size:16px;color:#fff}
.card-back .tagline{left:14px;top:36px;font-size:5px;color:#eaf3fb}

.envelope{left:450px;top:749px;width:345px;height:162px}
.envelope .contact{left:96px;top:60px;font-size:5px}

.envelope-back{left:817px;top:744px;width:334px;height:167px}
.envelope-back .flap{position:absolute;left:0;top:0;width:100%;height:70px}
.envelope-back .web{top:22px;font-size:8px}
</style>
</head>
<body>

<section class="sheet letterhead" aria-label="Letterhead">
  <div class="brand"><span class="dot"></span><span class="name">Bright Ferns</span></div>
  <p class="tagline">Natural Wellness &amp; Live Cell Review</p>
  <address class="contact">Marla Dunwoody<br>2736-18 Avenue, Suite 200<br>Larkvale, AB T8K 2P6<br>brightferns@mailnest.ca</address>
  <div class="faint-mark"></div>
  <svg class="swoosh" viewBox="0 0 400 240" preserveAspectRatio="none">
    <path d="M0,78 C120,40 270,8 400,4 L400,240 L0,240Z" fill="var(--blue)"/>
    <path d="M0,96 C130,62 270,34 400,30 L400,240 L0,240Z" fill="var(--black)"/>
    <path d="M0,120 C140,88 280,62 400,60" fill="none" stroke="var(--blue)" stroke-width="2"/>
  </svg>
  <p class="web">www.BrightFernsNaturalWellness.com</p>
</section>

<section class="sheet folder" aria-label="Presentation folder">
  <div class="brand"><span class="dot"></span><span class="name">Bright Ferns</span></div>
  <p class="tagline">Natural Wellness &amp; Live Cell Review</p>
  <svg class="swoosh" viewBox="0 0 400 240" preserveAspectRatio="none">
    <path d="M0,34 C140,52 280,76 400,110 L400,240 L0,240Z" fill="var(--blue)"/>
    <path d="M0,52 C140,70 280,96 400,132 L400,240 L0,240Z" fill="var(--black)"/>
    <path d="M0,74 C140,92 280,120 400,156" fill="none" stroke="var(--blue)" stroke-width="1.5"/>
  </svg>
  <p class="web">www.BrightFernsNaturalWellness.com</p>
</section>

<section class="sheet card-front" aria-label="Business card front">
  <div class="brand"><span class="dot"></span><span class="name">Bright Ferns</span></div>
  <p class="tagline">Natural Wellness &amp; Live Cell Review</p>
  <address class="contact">Marla Dunwoody, DynBC, CH, BA<br>brightferns@mailnest.ca</address>
  <svg class="swoosh" viewBox="0 0 400 60" preserveAspectRatio="none">
    <path d="M0,10 C140,20 280,30 400,22 L400,60 L0,60Z" fill="var(--blue)"/>
    <path d="M0,22 C140,32 280,40 400,32 L400,60 L0,60Z" fill="var(--black)"/>
  </svg>
</section>

<section class="sheet card-back" aria-label="Business card back">
  <div class="brand"><span class="dot"></span><span class="name">Bright Ferns</span></div>
  <p class="tagline">Natural Wellness &amp; Live Cell Review</p>
</section>

<section class="sheet envelope" aria-label="Envelope front">
  <address class="contact">Larkvale Acupuncture Clinic<br>2736-18 Avenue, Suite 200<br>Larkvale, AB T8K 2P6</address>
</section>

<section class="sheet envelope-back" aria-label="Envelope back">
  <svg class="flap" viewBox="0 0 400 80" preserveAspectRatio="none">
    <path d="M0,0 L400,0 L400,58 C300,80 100,80 0,58Z" fill="var(--black)"/>
  </svg>
  <p class="web">www.BrightFernsNaturalWellness.com</p>
</section>

</body>
</html>
```